Bright Harbor Concierge

I need a website developed for our travel concierge service. I'm looking to be able to collect information and have the information collected directed to a inbox. I would also like to me able to manage the updates to the website myself. I also would like a mobile version of the website to be included. Our services include assistance with Bachelor Parties, Bachelorette Parties and Medical Tourism. We provide custom packages that include Airport Transportation, Lodging, Bilingual guides and any other special needs identified by our clients.
Industry/Entity Type
Travel
Coding
Coded - Design and coding required
Number of Pages Required
4 page
Look and feel

```html
<!DOCTYPE html>
<html lang="en">
<head>
<meta charset="utf-8">
<title>Bright Harbor Concierge</title>
<link rel="stylesheet" href="https://fonts.googleapis.com/css2?family=Cinzel:wght@400;500&family=Mulish:wght@400;500;600&family=Libre+Baskerville&display=swap">
<style>
:root{
  --gold:#c8922a;
  --gold-soft:#e7cf9e;
  --ink:#0c0a0f;
  --night:#15101c;
  --text:#3c3c3c;
  --light:#f1f1f2;
  --white:#ffffff;
  --footer-band:#1c1c1c;
}
*{margin:0;padding:0;box-sizing:border-box}
html,body{width:1200px;height:3967px;overflow:hidden}
body{position:relative;font-family:'Mulish',sans-serif;color:var(--text);background:var(--white)}
.abs{position:absolute}
.title{font-family:'Cinzel',serif;font-weight:400;color:var(--gold);line-height:1}
.mark{width:26px;height:26px;border:2px solid var(--gold);border-radius:50%;opacity:.8}
.btn{position:absolute;background:#000;color:#fff;font-family:'Mulish',sans-serif;font-weight:600;font-size:16px;letter-spacing:1.5px;display:flex;align-items:center;justify-content:center}

/* hero menu */
.hero{left:0;top:0;width:1200px;height:533px;background:radial-gradient(ellipse at 40% 40%,#2a2030 0%,#14101a 55%,#08070a 100%)}
.brand{left:0;width:1200px;text-align:center}
.brand-dot{width:40px;height:40px;border:2px solid var(--gold);border-radius:50%;margin:0 auto 8px}
.brand-name{font-family:'Cinzel',serif;color:var(--gold);font-size:20px;letter-spacing:1px}
.menu-title{left:0;top:174px;width:1200px;text-align:center;font-size:44px}
.menu-list{left:420px;top:236px;width:360px;list-style:none;text-align:center}
.menu-list li{height:50px;line-height:46px;font-size:13px;letter-spacing:1.5px;color:#fff;font-weight:500;border-bottom:1px solid rgba(255,255,255,.25)}
.menu-list li:last-child{border-bottom:none}
.close{left:1006px;top:46px}

/* about */
.about-title{left:159px;top:664px;font-size:44px}
.about-copy{left:159px;top:736px;width:420px;font-size:16px;line-height:28px;color:#333}
.about-photo{left:570px;top:600px;width:580px;height:427px;background:radial-gradient(ellipse at 50% 50%,#9a9a9a 0%,#c9c9c9 45%,rgba(255,255,255,0) 72%)}

/* services */
.services{left:0;top:1126px;width:1200px;height:584px;background:radial-gradient(ellipse at 50% 40%,#2b1f36 0%,#171020 55%,#0b080e 100%)}
.services-title{left:0;top:1196px;width:1200px;text-align:center;font-size:42px}
.service{top:1305px;width:260px;text-align:center}
.service-photo{position:relative;margin:0 auto;width:204px;height:204px}
.service-photo .pic{position:absolute;left:12px;top:12px;width:176px;height:176px;border-radius:50%;border:4px solid #fff}
.service-photo svg{position:absolute;left:0;top:0}
.service h3{font-family:'Cinzel',serif;font-weight:400;color:var(--gold);font-size:19px;margin-top:10px}
.service p{color:#fff;font-size:11px;line-height:18px;margin-top:8px}
.service a{display:inline-block;margin-top:12px;color:var(--gold);font-size:11px;letter-spacing:1.5px;font-weight:600;text-decoration:none;border-bottom:1px solid var(--gold);padding-bottom:2px}

/* packages */
.packages{left:0;top:1710px;width:1200px;height:712px;background:linear-gradient(180deg,#e6e6e8 0%,#f2f2f3 50%,#fafafa 100%)}
.pk-title{font-family:'Cinzel',serif;fill:var(--ink)}
.pk-body{font-family:'Mulish',sans-serif;fill:#555;font-size:15px}

/* newsletter */
.news-photo{left:0;top:2422px;width:1200px;height:320px;background:linear-gradient(90deg,#4a3a36 0%,#6b5048 30%,#7a4a48 55%,#4e4b56 80%,#3a3640 100%)}
.news-box{left:234px;top:2603px;width:733px;height:270px;background:#000;text-align:center}
.news-box h2{font-size:42px;margin-top:44px}
.news-box .mark{margin:10px auto 0}
.news-box p{color:#bbb;font-size:15px;margin-top:8px}
.news-input{position:absolute;left:185px;top:165px;width:370px;height:51px;background:#fff;display:flex;align-items:center;justify-content:center;font-family:'Libre Baskerville',serif;font-size:16px;color:#333}
.news-input svg{position:absolute;right:14px;top:16px}

/* contact form */
.contact-photo{left:678px;top:2804px;width:522px;height:562px;background:radial-gradient(ellipse at 60% 50%,#e8d49a 0%,#f1e4c2 40%,rgba(255,255,255,0) 75%)}
.contact-title{left:159px;top:2910px;font-size:42px}
.field{position:absolute;border:1px solid #bbb;background:#fff;font-size:15px;color:#555;padding:8px 10px}

/* info band */
.info{left:0;top:3366px;width:1200px;height:228px;background:var(--footer-band)}
.info-col{top:3444px;width:300px;text-align:center}
.info-col h4{font-family:'Libre Baskerville',serif;font-weight:400;color:var(--gold);font-size:14px;letter-spacing:1px}
.info-col p{color:#ddd;font-size:13px;letter-spacing:1px;line-height:20px;margin-top:16px}
.divider{top:3428px;width:1px;height:162px;background:#555}

/* footer */
.footer{left:0;top:3594px;width:1200px;height:328px;background:#000}
.footer-copy{left:0;top:3742px;width:1200px;text-align:center;font-family:'Libre Baskerville',serif;color:#ddd;font-size:12px;line-height:22px}
.footer-nav{left:0;top:3866px;width:1200px;text-align:center;font-size:10px;letter-spacing:1px;color:var(--gold)}
.footer-nav span{margin:0 14px}
.footer-nav i{display:inline-block;width:5px;height:5px;border-radius:50%;background:var(--gold);vertical-align:middle}
.copyright{left:0;top:3922px;width:1200px;height:45px;background:#b7891c;color:#fff;font-size:10px;text-align:center;line-height:45px}
</style>
</head>
<body>

<!-- Hero with menu overlay -->
<section class="abs hero" role="img" aria-label="Dimmed photo of friends celebrating at a party behind the menu overlay"></section>
<div class="abs brand" style="top:40px">
  <div class="brand-dot"></div>
  <div class="brand-name">Bright Harbor Concierge</div>
</div>
<svg class="abs close" width="36" height="36" viewBox="0 0 36 36"><path d="M2 2L34 34M34 2L2 34" stroke="#c8922a" stroke-width="2"/></svg>
<h2 class="abs title menu-title">Menu</h2>
<ul class="abs menu-list">
  <li>HOME</li><li>ABOUT US</li><li>SERVICES</li><li>CONTACT</li>
</ul>

<!-- About -->
<div class="abs about-photo" role="img" aria-label="Black and white photo of friends toasting with champagne glasses"></div>
<h2 class="abs title about-title">About Us</h2>
<div class="abs mark" style="left:160px;top:706px"></div>
<p class="abs about-copy">Lorem ipsum dolor sit amet, consectetur adipielit, sed do eiusmod tempor incididunt ut labore et dolore magna aliqua. Quis ipsum suspendisse ultrices gravida. Risus commodo viverra maecenas vel facilisis.</p>
<div class="btn" style="left:156px;top:886px;width:176px;height:52px">READ MORE</div>

<!-- Services -->
<section class="abs services" role="img" aria-label="Dark photo of a crowd dancing at a night party"></section>
<h2 class="abs title services-title">Our Services</h2>
<div class="abs mark" style="left:587px;top:1245px"></div>

<div class="abs service" style="left:144px">
  <div class="service-photo">
    <div class="pic" role="img" aria-label="Photo of men toasting beers at a bar" style="background:radial-gradient(circle,#8a5a7a,#3a2440)"></div>
    <svg width="204" height="204" viewBox="0 0 204 204"><path d="M120 6 A98 98 0 1 1 10 120" fill="none" stroke="#c8922a" stroke-width="4"/></svg>
  </div>
  <h3>Bachelor Parties</h3>
  <p>Lorem ipsum dolor sit amet, coctetur<br>adipielit, sed do eiusm</p>
  <a>READ MORE</a>
</div>
<div class="abs service" style="left:471px">
  <div class="service-photo">
    <div class="pic" role="img" aria-label="Photo of women celebrating a bachelorette party with decorations" style="background:radial-gradient(circle,#f0d8e0,#c998b0)"></div>
    <svg width="204" height="204" viewBox="0 0 204 204"><path d="M120 6 A98 98 0 1 1 10 120" fill="none" stroke="#c8922a" stroke-width="4"/></svg>
  </div>
  <h3>Bachelorette Parties</h3>
  <p>Lorem ipsum dolor sit amet, coctetur<br>adipielit, sed do eiusm</p>
  <a>READ MORE</a>
</div>
<div class="abs service" style="left:807px">
  <div class="service-photo">
    <div class="pic" role="img" aria-label="Photo of a traveler in a suit with luggage at an airport" style="background:radial-gradient(circle,#c8d0d8,#5a6470)"></div>
    <svg width="204" height="204" viewBox="0 0 204 204"><path d="M120 6 A98 98 0 1 1 10 120" fill="none" stroke="#c8922a" stroke-width="4"/></svg>
  </div>
  <h3>Medical Tourism</h3>
  <p>Lorem ipsum dolor sit amet, coctetur<br>adipielit, sed do eiusm</p>
  <a>READ MORE</a>
</div>

<!-- Custom packages -->
<section class="abs packages" role="img" aria-label="Faded photo of people socialising behind the packages">
<svg width="1200" height="712" viewBox="0 0 1200 712">
  <text x="600" y="112" text-anchor="middle" font-family="Cinzel,serif" font-size="40" fill="#c8922a">CUSTOM PACKAGES</text>
  <circle cx="600" cy="140" r="12" fill="none" stroke="#c8922a" stroke-width="2" opacity=".8"/>

  <!-- Airport -->
  <g transform="translate(305 320)">
    <path d="M0-141L144 0L0 141L-144 0Z" fill="#fff" stroke="#c8922a" stroke-width="1.5"/>
    <path d="M0-141L70-71L-70-71Z" fill="#c8922a"/>
    <path d="M-38 103L38 103L0 141Z" fill="#000"/>
    <path d="M-22-88L22-88M-4-98L6-88L-4-80M-14-92L-10-88L-14-84" stroke="#fff" stroke-width="3" fill="none"/>
    <path d="M-10 120L10 120M4 114L10 120L4 126" stroke="#c8922a" stroke-width="1.5" fill="none"/>
    <text class="pk-title" x="0" y="-40" text-anchor="middle" font-size="19">AIRPORT</text>
    <text class="pk-title" x="0" y="-15" text-anchor="middle" font-size="19">TRANSPORTATION</text>
    <text class="pk-body" x="0" y="20" text-anchor="middle">suspendisse ultces grda</text>
    <text class="pk-body" x="0" y="42" text-anchor="middle">Risus commodo</text>
    <text class="pk-body" x="0" y="64" text-anchor="middle">maecenas</text>
  </g>
  <!-- Lodging -->
  <g transform="translate(601 320)">
    <path d="M0-141L144 0L0 141L-144 0Z" fill="#fff" stroke="#c8922a" stroke-width="1.5"/>
    <path d="M0-141L70-71L-70-71Z" fill="#c8922a"/>
    <path d="M-38 103L38 103L0 141Z" fill="#000"/>
    <rect x="-12" y="-108" width="24" height="28" fill="#fff"/>
    <rect x="-22" y="-96" width="10" height="16" fill="#fff"/>
    <rect x="12" y="-98" width="10" height="18" fill="#fff"/>
    <path d="M-10 120L10 120M4 114L10 120L4 126" stroke="#c8922a" stroke-width="1.5" fill="none"/>
    <text class="pk-title" x="0" y="-28" text-anchor="middle" font-size="19">LODGING</text>
    <text class="pk-body" x="0" y="12" text-anchor="middle">suspendisse ultces grda</text>
    <text class="pk-body" x="0" y="34" text-anchor="middle">Risus commodo</text>
    <text class="pk-body" x="0" y="56" text-anchor="middle">maecenas</text>
  </g>
  <!-- Bilingual -->
  <g transform="translate(898 320)">
    <path d="M0-141L144 0L0 141L-144 0Z" fill="#fff" stroke="#c8922a" stroke-width="1.5"/>
    <path d="M0-141L70-71L-70-71Z" fill="#c8922a"/>
    <path d="M-38 103L38 103L0 141Z" fill="#000"/>
    <rect x="-16" y="-112" width="12" height="9" fill="#fff"/>
    <rect x="4" y="-112" width="12" height="9" fill="#fff"/>
    <circle cx="0" cy="-94" r="5" fill="#fff"/>
    <path d="M-10-80Q0-92 10-80Z" fill="#fff"/>
    <path d="M-10 120L10 120M4 114L10 120L4 126" stroke="#c8922a" stroke-width="1.5" fill="none"/>
    <text class="pk-title" x="0" y="-40" text-anchor="middle" font-size="19">BILINGUAL</text>
    <text class="pk-title" x="0" y="-15" text-anchor="middle" font-size="19">GUIDES</text>
    <text class="pk-body" x="0" y="20" text-anchor="middle">suspendisse ultces grda</text>
    <text class="pk-body" x="0" y="42" text-anchor="middle">Risus commodo</text>
    <text class="pk-body" x="0" y="64" text-anchor="middle">maecenas</text>
  </g>
  <!-- Special needs -->
  <g transform="translate(453 484)">
    <path d="M0-141L144 0L0 141L-144 0Z" fill="#fff" stroke="#c8922a" stroke-width="1.5"/>
    <path d="M0-141L70-71L-70-71Z" fill="#c8922a"/>
    <path d="M-38 103L38 103L0 141Z" fill="#000"/>
    <circle cx="0" cy="-90" r="8" fill="none" stroke="#fff" stroke-width="2.5"/>
    <circle cx="-2" cy="-108" r="3" fill="#fff"/>
    <path d="M-10 120L10 120M4 114L10 120L4 126" stroke="#c8922a" stroke-width="1.5" fill="none"/>
    <text class="pk-title" x="0" y="-28" text-anchor="middle" font-size="19">SPECIAL NEEDS</text>
    <text class="pk-body" x="0" y="12" text-anchor="middle">suspendisse ultces grda</text>
    <text class="pk-body" x="0" y="34" text-anchor="middle">Risus commodo</text>
    <text class="pk-body" x="0" y="56" text-anchor="middle">maecenas</text>
  </g>
  <!-- Many more -->
  <g transform="translate(750 484)">
    <path d="M0-141L144 0L0 141L-144 0Z" fill="#fff" stroke="#c8922a" stroke-width="1.5"/>
    <path d="M0-141L70-71L-70-71Z" fill="#c8922a"/>
    <path d="M-38 103L38 103L0 141Z" fill="#000"/>
    <path d="M-10-110L6-110L12-104L12-80L-10-80Z" fill="#fff"/>
    <path d="M-5-90L-5-84M0-92L0-84M5-90L5-84" stroke="#c8922a" stroke-width="2"/>
    <path d="M-10 120L10 120M4 114L10 120L4 126" stroke="#c8922a" stroke-width="1.5" fill="none"/>
    <text class="pk-title" x="0" y="-40" text-anchor="middle" font-size="19">AND MANY</text>
    <text class="pk-title" x="0" y="-15" text-anchor="middle" font-size="19">MORE</text>
    <text class="pk-body" x="0" y="20" text-anchor="middle">suspendisse ultces grda</text>
    <text class="pk-body" x="0" y="42" text-anchor="middle">Risus commodo</text>
    <text class="pk-body" x="0" y="64" text-anchor="middle">maecenas</text>
  </g>
</svg>
</section>

<!-- Newsletter -->
<div class="abs news-photo" role="img" aria-label="Photo of friends sharing drinks around a restaurant table"></div>
<div class="abs news-box">
  <h2 class="title">Stay In Touch</h2>
  <div class="mark"></div>
  <p>Signup to recieve news and updates from Bright Harbor Concierge</p>
  <div class="news-input">Enter your e-mail
    <svg width="20" height="20" viewBox="0 0 20 20"><path d="M2 10L18 2L12 18L9 11Z M9 11L18 2" fill="none" stroke="#c8922a" stroke-width="1.5"/></svg>
  </div>
</div>

<!-- Contact form -->
<div class="abs contact-photo" role="img" aria-label="Soft photo of champagne glasses on a table"></div>
<h2 class="abs title contact-title">Get In Touch</h2>
<div class="abs mark" style="left:160px;top:2958px"></div>
<div class="field" style="left:160px;top:3001px;width:237px;height:40px">Name</div>
<div class="field" style="left:404px;top:3001px;width:238px;height:40px">Email</div>
<div class="field" style="left:160px;top:3048px;width:237px;height:41px">Phone</div>
<div class="field" style="left:404px;top:3048px;width:238px;height:41px">Subject</div>
<div class="field" style="left:160px;top:3098px;width:482px;height:111px">Your Message</div>
<div class="btn" style="left:159px;top:3220px;width:176px;height:52px">SEND NOW</div>

<!-- Contact info -->
<section class="abs info"></section>
<div class="abs info-col" style="left:106px"><h4>LOCATION</h4><p>12 Quay Lane, Harbourview,<br>Coastline</p></div>
<div class="abs divider" style="left:433px"></div>
<div class="abs info-col" style="left:450px"><h4>PHONE</h4><p>02 555 014 271<br>02 555 014 272</p></div>
<div class="abs divider" style="left:758px"></div>
<div class="abs info-col" style="left:784px"><h4>EMAIL</h4><p>info@brightharborconcierge.com</p></div>

<!-- Footer -->
<footer class="abs footer"></footer>
<div class="abs brand" style="top:3640px">
  <div class="brand-dot"></div>
  <div class="brand-name">Bright Harbor Concierge</div>
</div>
<p class="abs footer-copy">Lorem ipsum dolor sit amet, consectetur adipiscing elit, sed<br>do eiusmod incididunt ut labore et dolore magna aliqua.<br>Quis ipsum suspendisse ultrices grada. Risus commodo<br>viverra maecenas aclacus vel facilisis.</p>
<div class="abs footer-nav"><span>HOME</span><i></i><span>ABOUT US</span><i></i><span>SERVICES</span><i></i><span>CONTACT</span></div>
<div class="abs copyright">© 2021 Bright Harbor Concierge. All right reserved.</div>

</body>
</html>
```